A website for Bloom Care, a multidisciplnary approach to treating development and functional issue

We need a simple, clean interface, that is intuitive.

We want parents to be able to be impressed by our services, and be able to trust our team and get simple easy to understand information about their child's potential condition and our therapists.

We also want the website to be mobile friendly and easy to integrate into social media as this will be how we attract people to our website.

Proper coding would be excellent too so that we have functionality and it can be easily changed

Target Market(s)

Parents, teachers, children, families

Number of Pages Required

5+ page

Font styles to use
Sans Serif

Colors
105da8
fbee3d
ec1f27

Requirements
Must have
• Social media functionality.
• Be bright simple and interesting.

```html
<!DOCTYPE html>
<html lang="en">
<head>
<meta charset="UTF-8">
<title>Bloom Care</title>
<link href="https://fonts.googleapis.com/css2?family=Delius&family=Open+Sans:wght@400;600;700&display=swap" rel="stylesheet">
<style>
:root{
  --blue:#105da8;
  --blue-deep:#0f3f8e;
  --yellow:#fbee3d;
  --red:#ec1f27;
  --white:#ffffff;
  --text:#444;
  --muted:#8a8a8a;
}
*{margin:0;padding:0;box-sizing:border-box}
html,body{width:718px;height:1200px;overflow:hidden}
body{background:var(--yellow);font-family:'Open Sans',sans-serif;position:relative;color:var(--text)}
.abs{position:absolute}
.hand{font-family:'Delius',cursive}

/* header panel */
.header-panel{left:58px;top:33px;width:600px;height:371px;background:var(--white);box-shadow:0 10px 12px -8px rgba(0,0,0,.35)}
.brand{left:76px;top:52px;display:flex;align-items:center;gap:6px;font-family:'Delius',cursive;font-size:15px;color:var(--blue)}
.brand-dot{width:12px;height:12px;border-radius:50%;background:var(--red)}
.nav{top:60px;right:78px;display:flex;gap:25px;font-family:'Delius',cursive;font-size:10px;color:var(--blue)}
.nav .active{color:var(--red);position:relative}
.nav-marker{left:363px;top:33px;width:40px;height:4px;background:var(--red)}

.hero{left:66px;top:100px;width:584px;height:296px;background:linear-gradient(100deg,#6e4e3c 0%,#a68268 40%,#e8c6a8 70%,#c9a07e 100%)}
.hero-circle-blue{left:106px;top:154px;width:204px;height:204px;border-radius:50%;background:var(--blue-deep);opacity:.95}
.hero-circle-red{left:270px;top:248px;width:100px;height:100px;border-radius:50%;background:var(--red);mix-blend-mode:multiply}
.hero-copy{left:116px;top:200px;width:184px;text-align:center;color:var(--white)}
.hero-title{font-family:'Delius',cursive;font-size:23px;line-height:1}
.hero-text{font-size:8.5px;line-height:11.5px;margin-top:12px}
.btn-start{left:158px;top:286px;width:99px;height:24px;background:var(--red);color:var(--white);font-family:'Delius',cursive;font-size:9.5px;display:flex;align-items:center;justify-content:center}
.dots{left:339px;top:369px;display:flex;gap:6px}
.dots span{width:6px;height:6px;border-radius:50%;background:var(--white)}
.dots span.on{background:var(--yellow)}

/* services */
.section-title{left:0;width:718px;top:422px;text-align:center;font-family:'Delius',cursive;font-size:21px;color:var(--blue)}
.service{top:466px;width:185px}
.service-img{height:107px}
.service-name{font-family:'Delius',cursive;font-size:9px;color:var(--blue);margin-top:17px}
.service-text{font-size:6.6px;line-height:11.3px;color:var(--muted);margin-top:12px;padding-left:1px}
.btn-more{display:inline-block;margin-top:16px;background:var(--red);color:var(--white);font-family:'Delius',cursive;font-size:7px;padding:3px 9px;border-radius:2px}

/* testimonials */
.testi-img{left:66px;top:730px;width:285px;height:207px;background:linear-gradient(120deg,#d8d2c6 0%,#9c6a46 45%,#e0b12a 75%,#7a4a2c 100%)}
.testi{left:351px;top:730px;width:300px;height:207px;background:var(--blue)}
.testi-title{left:12px;top:12px;font-family:'Delius',cursive;font-size:20px;color:var(--white)}
.testi-arrows{right:12px;top:18px}
.testi-quote{left:10px;top:55px;font-family:Georgia,serif;font-size:32px;color:var(--white);line-height:1}
.testi-text{left:20px;top:96px;width:260px;text-align:center;color:var(--white);font-size:8.6px;line-height:11.3px}
.testi-name{left:0;width:300px;top:154px;text-align:center;color:var(--white);font-size:8.6px}
.testi-name b{font-family:'Delius',cursive;font-weight:700}
.testi-city{left:0;width:300px;top:172px;text-align:center;color:var(--white);font-size:6.5px;font-weight:700}

/* feature tiles */
.tile{top:962px;width:185px;height:144px}
.tile-img{height:107px;position:relative}
.tile-bar{height:37px;background:var(--red);display:flex;align-items:center;justify-content:space-between;padding:0 10px;font-family:'Delius',cursive;font-size:9.5px;color:var(--white)}

/* footer */
.footer{left:58px;top:1125px;width:600px;height:53px;background:var(--white);box-shadow:0 8px 10px -7px rgba(0,0,0,.3)}
.footer-links{left:10px;top:9px;display:flex;font-family:'Delius',cursive;font-size:9.5px;color:#333}
.footer-links span{padding:0 14px 0 0}
.footer-links .sep{padding:0 14px 0 0}
.copyright{left:10px;top:29px;font-family:'Delius',cursive;font-size:9.5px;color:#333}
.social{right:8px;top:18px;display:flex;gap:2.5px}
.social span{width:16px;height:16px;border-radius:50%}
</style>
</head>
<body>

<div class="abs header-panel"></div>
<div class="abs nav-marker"></div>
<div class="abs brand"><span class="brand-dot"></span>Bloom Care</div>
<nav class="abs nav">
  <span class="active">Home</span><span>About Us</span><span>Services</span><span>FAQ's</span><span>Contact Us</span>
</nav>

<div class="abs hero" role="img" aria-label="Photo of a smiling young girl with pigtails, parents in the background"></div>
<div class="abs hero-circle-blue"></div>
<div class="abs hero-circle-red"></div>
<div class="abs hero-copy">
  <div class="hero-title">Bloom Care</div>
  <p class="hero-text">Neque porro quisquam est qui dolorem ipsum quia dolor sit amet, consectetur, adipisci velit...</p>
</div>
<div class="abs btn-start">Get Started</div>
<div class="abs dots"><span class="on"></span><span></span><span></span><span></span></div>

<h2 class="abs section-title">Our Services</h2>

<div class="abs service" style="left:66px">
  <div class="service-img" role="img" aria-label="Photo of a father and son playing with building blocks" style="background:linear-gradient(135deg,#e6ddd0,#b08a6a 55%,#d0392e)"></div>
  <div class="service-name">Neuro Developmental Therapy</div>
  <p class="service-text">Lorem Ipsum is simply dummy text of the printing and typesetting industry. Lorem Ipsum has been the industry's standard dummy text ever since the 1500s, when an unknown printer took a galley of type and scrambled it to make a type specimen book.</p>
  <span class="btn-more">Read More</span>
</div>
<div class="abs service" style="left:266px">
  <div class="service-img" role="img" aria-label="Photo of a family talking with a therapist" style="background:linear-gradient(135deg,#eef0f2,#7b8fb0 50%,#c9a58a)"></div>
  <div class="service-name">Behaviour Therapy</div>
  <p class="service-text">Lorem Ipsum is simply dummy text of the printing and typesetting industry. Lorem Ipsum has been the industry's standard dummy text ever since the 1500s, when an unknown printer took a galley of type and scrambled it to make a type specimen book.</p>
  <span class="btn-more">Read More</span>
</div>
<div class="abs service" style="left:466px">
  <div class="service-img" role="img" aria-label="Photo of a girl reading with a teacher in a classroom" style="background:linear-gradient(135deg,#f0e6df,#d88aa0 45%,#3f7fd0)"></div>
  <div class="service-name">Handwriting Training</div>
  <p class="service-text">Lorem Ipsum is simply dummy text of the printing and typesetting industry. Lorem Ipsum has been the industry's standard dummy text ever since the 1500s, when an unknown printer took a galley of type and scrambled it to make a type specimen book.</p>
  <span class="btn-more">Read More</span>
</div>

<div class="abs testi-img" role="img" aria-label="Photo of a mother and daughter smiling over a tablet"></div>
<div class="abs testi">
  <div class="abs testi-title">Testimonials</div>
  <svg class="abs testi-arrows" width="30" height="12" viewBox="0 0 30 12" aria-hidden="true">
    <path d="M6 1 L1 6 L6 11" fill="none" stroke="#fff" stroke-width="1.8"/>
    <path d="M23 1 L28 6 L23 11" fill="none" stroke="#fff" stroke-width="1.8"/>
  </svg>
  <div class="abs testi-quote">&ldquo;</div>
  <p class="abs testi-text">Lorem Ipsum is simply dummy text of the printing and typesetting industry. Lorem Ipsum has been the industry's standard dummy text ever since the 1500s, when an unknown printer took a galley of type and scrambled it to make a type specimen book.</p>
  <div class="abs testi-name"><b>Nora Hale</b> Mother Of Lily Hale</div>
  <div class="abs testi-city">Riverton</div>
</div>

<div class="abs tile" style="left:66px">
  <div class="tile-img" role="img" aria-label="Photo of a boy playing football in a park" style="background:linear-gradient(180deg,#b9c7a0,#6f9a48 60%,#4e7a30)">
    <svg class="abs" style="left:78px;top:40px" width="28" height="28" viewBox="0 0 28 28" aria-hidden="true">
      <circle cx="14" cy="14" r="13" fill="rgba(255,255,255,.85)"/>
      <path d="M11 8 L20 14 L11 20 Z" fill="#333"/>
    </svg>
  </div>
  <div class="tile-bar">Our Videos
    <svg width="11" height="11" viewBox="0 0 11 11" aria-hidden="true"><circle cx="5.5" cy="5.5" r="5.5" fill="#fff"/><path d="M4.3 3 L6.8 5.5 L4.3 8" fill="none" stroke="#ec1f27" stroke-width="1.5"/></svg>
  </div>
</div>
<div class="abs tile" style="left:266px">
  <div class="tile-img" role="img" aria-label="Photo of a father drawing with his children" style="background:linear-gradient(135deg,#8a5a3c,#c9a58a 50%,#9a9aa0)"></div>
  <div class="tile-bar">Our Gallery
    <svg width="11" height="11" viewBox="0 0 11 11" aria-hidden="true"><circle cx="5.5" cy="5.5" r="5.5" fill="#fff"/><path d="M4.3 3 L6.8 5.5 L4.3 8" fill="none" stroke="#ec1f27" stroke-width="1.5"/></svg>
  </div>
</div>
<div class="abs tile" style="left:466px">
  <div class="tile-img" role="img" aria-label="Photo of a happy family hugging" style="background:linear-gradient(135deg,#f3ece6,#e2b99a 50%,#c88a64)"></div>
  <div class="tile-bar">Our Stories
    <svg width="11" height="11" viewBox="0 0 11 11" aria-hidden="true"><circle cx="5.5" cy="5.5" r="5.5" fill="#fff"/><path d="M4.3 3 L6.8 5.5 L4.3 8" fill="none" stroke="#ec1f27" stroke-width="1.5"/></svg>
  </div>
</div>

<footer class="abs footer">
  <div class="abs footer-links">
    <span>Home</span><span class="sep">|</span><span>About Us</span><span class="sep">|</span><span>Services</span><span class="sep">|</span><span>FAQ's</span><span class="sep">|</span><span>Contact Us</span>
  </div>
  <div class="abs copyright">&copy; 2015 Company Name,All Rights Reserved</div>
  <div class="abs social" aria-label="Social links">
    <span style="background:#3b5998"></span>
    <span style="background:#2aa9e0"></span>
    <span style="background:#d9251d"></span>
    <span style="background:#0e76a8"></span>
    <span style="background:#dd4b39"></span>
    <span style="background:#f26522"></span>
  </div>
</footer>

</body>
</html>
```